luxury contemporary fashion website needs simple, elegant flowchart to describe the buying and selli

* Luxury, resale, preloved items are sold on this online platform
*Horizontal, simple, flowchart with 5 steps in 'friendly' font with a simple emoticon/ picture for each step
*To be positioned in the 'How we work' tab of the webpage to explain in a very simple manner the buying and selling process for the customers.
*Attached is a very rudimentary mock-up of what we would like included and an idea of a project similar to what we desire
* to confirm the text for each step, we have also attached a word file below

Industry/Entity Type

Fashion

Font styles to use
Sans Serif

Colors
86cfc6
cfeae6

Requirements
Must have
• Simple drawing / shape after each point In the closest to 'duck egg blue' fill colour you can find with a black outline

```html
<!DOCTYPE html>
<html lang="en">
<head>
<meta charset="utf-8">
<title>Bespoke Concierge Service</title>
<link rel="stylesheet" href="https://fonts.googleapis.com/css2?family=Arimo:ital,wght@0,400;0,700;1,400;1,700&display=swap">
<style>
  :root {
    --duck-egg: #86cfc6;
    --duck-egg-light: #cfeae6;
    --ink: #111111;
    --ribbon: #0b0b0b;
    --ribbon-fold: #2a2a2a;
    --paper: #ffffff;
    --shadow: rgba(0, 0, 0, 0.18);
  }
  * { box-sizing: border-box; margin: 0; padding: 0; }
  html, body {
    width: 1200px; height: 750px; overflow: hidden;
    background: var(--paper);
    font-family: "Arimo", Arial, sans-serif;
    color: var(--ink);
  }
  .canvas { position: relative; width: 1200px; height: 750px; }

  .panel {
    position: absolute; left: 10px; top: 80px; width: 1176px; height: 604px;
    background: var(--duck-egg);
    box-shadow: 0 2px 6px var(--shadow);
  }
  .panel::after {
    content: ""; position: absolute; left: 0; right: 0; bottom: -8px; height: 8px;
    background:
      linear-gradient(135deg, var(--duck-egg) 5.5px, transparent 0) 0 0 / 11px 8px repeat-x,
      linear-gradient(225deg, var(--duck-egg) 5.5px, transparent 0) 0 0 / 11px 8px repeat-x;
  }

  .ribbon { position: absolute; left: 290px; top: 24px; width: 680px; height: 100px; }
  .ribbon-title {
    position: absolute; left: 325px; top: 29px; width: 610px; height: 70px;
    display: flex; align-items: center; justify-content: center;
    color: var(--paper); font-weight: 700; font-size: 31px; letter-spacing: -0.2px;
  }

  .flow-lines { position: absolute; left: 0; top: 0; width: 1200px; height: 750px; }

  .step { position: absolute; text-align: center; }
  .step-number {
    display: inline-flex; align-items: center; justify-content: center;
    width: 34px; height: 34px; border: 3px solid var(--ink); border-radius: 50%;
    font-weight: 700; font-size: 20px; line-height: 1;
  }
  .step-title { font-weight: 700; font-size: 25px; line-height: 30px; margin-top: 12px; }
  .step-note { font-style: italic; font-size: 15.5px; line-height: 19.5px; margin-top: 6px; }
  .step-note--small { font-size: 12.5px; line-height: 15px; margin-top: 8px; }
  .icon { display: inline-block; vertical-align: middle; }

  .step--have   { left: 14px;  top: 370px; width: 180px; }
  .step--collect{ left: 184px; top: 231px; width: 180px; }
  .step--prepare{ left: 383px; top: 231px; width: 180px; }
  .step--sold   { left: 580px; top: 231px; width: 180px; }

  .payment-number { position: absolute; left: 870px; top: 292px; }
  .payment-label {
    position: absolute; left: 820px; top: 356px; width: 150px;
    text-align: center; font-weight: 700; font-size: 22px; line-height: 27px;
  }
  .option { position: absolute; font-style: italic; font-size: 15.5px; line-height: 21px; }
  .option--cash { left: 960px; top: 272px; width: 150px; text-align: right; }
  .option--charity { left: 900px; top: 478px; width: 210px; text-align: right; }
  .currency { position: absolute; font-weight: 700; font-size: 26px; line-height: 1; }
  .currency--euro  { left: 1097px; top: 246px; }
  .currency--pound { left: 1128px; top: 230px; }
  .currency--dollar{ left: 1130px; top: 272px; }
  .emoticon-slot {
    position: absolute; width: 22px; height: 22px; border-radius: 50%;
    background: radial-gradient(circle at 50% 45%, var(--duck-egg-light) 0 45%, var(--ink) 75%);
  }
  .emoticon-slot--cool  { left: 508px; top: 468px; }
  .emoticon-slot--angel { left: 1134px; top: 513px; }
</style>
</head>
<body>
<main class="canvas">
  <section class="panel" aria-label="How we work"></section>

  <svg class="ribbon" viewBox="290 24 680 100" aria-hidden="true">
    <polygon points="290,52 345,52 345,114 290,114 308,83" fill="var(--ribbon)"/>
    <polygon points="970,52 915,52 915,114 970,114 952,83" fill="var(--ribbon)"/>
    <polygon points="325,99 345,114 345,99" fill="var(--ribbon-fold)"/>
    <polygon points="935,99 915,114 915,99" fill="var(--ribbon-fold)"/>
    <rect x="325" y="29" width="610" height="70" fill="var(--ribbon)"/>
  </svg>
  <h1 class="ribbon-title">Bespoke Concierge Service</h1>

  <svg class="flow-lines" viewBox="0 0 1200 750" aria-hidden="true">
    <path class="payment-cloud" d="M836 376 C820 366 828 346 848 352 C854 338 880 336 890 350 C902 336 932 338 936 354 C958 348 978 362 966 378 C982 390 972 412 952 408 C946 426 914 430 904 416 C892 430 860 428 856 412 C834 420 816 402 826 390 C812 386 818 372 836 376 Z"
          fill="var(--duck-egg)" stroke="var(--ink)" stroke-width="3"/>
    <line x1="972" y1="360" x2="1031" y2="302" stroke="var(--ink)" stroke-width="2.5"/>
    <line x1="982" y1="405" x2="1045" y2="461" stroke="var(--ink)" stroke-width="2.5"/>
    <g class="plane-icon" transform="translate(754 407)" fill="var(--ink)">
      <path d="M-26 -2 L18 -3 C26 -3 30 0 24 3 L-22 4 Z"/>
      <path d="M-4 -2 L6 -16 L12 -16 L6 -2 Z"/>
      <path d="M-4 3 L8 16 L14 16 L6 3 Z"/>
      <path d="M-26 -2 L-30 -12 L-24 -12 L-18 -2 Z"/>
    </g>
  </svg>

  <article class="step step--have">
    <span class="step-number">1</span>
    <h2 class="step-title">Have items<br>to sell?</h2>
    <p class="step-note">- brand spanking<br>or nearly new
      <svg class="icon" width="16" height="18" viewBox="0 0 16 18" aria-hidden="true">
        <g fill="var(--ink)">
          <polygon points="8,0 9.2,3 12,3.2 9.8,5 10.6,8 8,6.3 5.4,8 6.2,5 4,3.2 6.8,3"/>
          <polygon points="4,9 5,11.5 7.4,11.7 5.6,13.2 6.2,15.6 4,14.2 1.8,15.6 2.4,13.2 0.6,11.7 3,11.5"/>
          <polygon points="12,9 13,11.5 15.4,11.7 13.6,13.2 14.2,15.6 12,14.2 9.8,15.6 10.4,13.2 8.6,11.7 11,11.5"/>
        </g>
      </svg>
    </p>
  </article>

  <article class="step step--collect">
    <span class="step-number">2</span>
    <h2 class="step-title">Personal<br>collection</h2>
    <p class="step-note">- we choose<br>the pieces we know<br>the velora<br>customers will<br>love
      <svg class="icon" width="20" height="18" viewBox="0 0 20 18" aria-hidden="true">
        <path d="M10 17 L2 9 C-1 6 1 1 5 1 C7.5 1 9 3 10 4.5 C11 3 12.5 1 15 1 C19 1 21 6 18 9 Z" fill="var(--ink)"/>
      </svg>
    </p>
  </article>

  <article class="step step--prepare">
    <span class="step-number">3</span>
    <h2 class="step-title">We prepare</h2>
    <p class="step-note">-your item for sale<br>with thorough<br>authenticity &amp;<br>condition checks<br>from the velora<br>team ...</p>
    <p class="step-note step-note--small">so you don't<br>have to!</p>
  </article>
  <div class="emoticon-slot emoticon-slot--cool" role="img" aria-label="Emoticon: smiley wearing sunglasses"></div>

  <article class="step step--sold">
    <span class="step-number">4</span>
    <h2 class="step-title">Once sold</h2>
    <p class="step-note">- we lovingly<br>prepare the item<br>-shipped via<br>tracked services</p>
  </article>

  <span class="step-number payment-number">5</span>
  <h2 class="payment-label">Your<br>payment</h2>

  <p class="option option--cash">i) pocket the cash</p>
  <span class="currency currency--euro">€</span>
  <span class="currency currency--pound">£</span>
  <span class="currency currency--dollar">$</span>

  <p class="option option--charity">ii) donate to charity<br>-full or partial amount</p>
  <div class="emoticon-slot emoticon-slot--angel" role="img" aria-label="Emoticon: smiley with a halo"></div>
</main>
</body>
</html>
```